Ladles and Lanterns App design

I need a full app design, colours, images, fonts, and a mock up design of the app to bring to the developer.

Ladles and Lanterns is a free app that allows cafes, independent cafe and chains of cafes to let their customers know what the soup of the day and what specials they have on that day through the app. Each cafe will have a profile which they can upload the Ladles and Lanterns daily.

The user home screen will include google maps showing their location with the registered cafes and eateries around them. including a list of the cafe and distances below. as seen in attachment.

Target Market(s)

Cafes , anyone who enjoys eating soups and off local cafe specials boards

Requirements
Must have
• I would like a complete app design based on the attached images.

```html
<!DOCTYPE html>
<html lang="en">
<head>
<meta charset="utf-8">
<title>Ladles and Lanterns – App Screens</title>
<link rel="stylesheet" href="https://fonts.googleapis.com/css2?family=Lato:wght@400;700;900&display=swap">
<style>
:root{
  --canvas:#d6c3a3;
  --screen-bg:#ececec;
  --white:#ffffff;
  --brand-red:#d8432d;
  --accent-orange:#e0931a;
  --nav-dark:#333333;
  --text-dark:#333333;
  --text-mid:#555555;
  --price-green:#3f8f14;
  --border-light:#e2e2e2;
  --map-tone:#d9dcd3;
  --hero-dark:#4a3a2c;
  --hero-soup:#b9b07a;
}
*{box-sizing:border-box;margin:0;padding:0}
html,body{width:1200px;height:797px;overflow:hidden;background:var(--canvas);font-family:'Lato',Arial,sans-serif;color:var(--text-dark)}
.stage{position:absolute;left:0;top:0;width:1520px;height:1010px;transform:scale(0.78947);transform-origin:0 0}
.phone{position:absolute;top:44px;width:450px;height:900px;background:var(--screen-bg);overflow:hidden}
.phone--map{left:37px}.phone--menu{left:526px}.phone--detail{left:1015px}
.app-header{position:absolute;left:0;top:0;width:100%;height:69px;background:var(--white);z-index:3;text-align:center}
.app-title{font-weight:900;font-size:30px;line-height:69px;color:var(--brand-red);letter-spacing:.2px}
.brand-dot{position:absolute;left:174px;top:10px;width:102px;height:104px;border-radius:50%;background:var(--white);z-index:2}
.map-area{position:absolute;left:0;top:69px;width:100%;height:345px;background:linear-gradient(160deg,#dfe2d8,#cfd6c8 55%,#d9dcd3)}
.hero{position:absolute;left:0;top:69px;width:100%;height:172px;background:radial-gradient(ellipse at 52% 55%,var(--hero-soup) 0,#8c8a4c 32%,#3d5a2a 52%,var(--hero-dark) 75%)}
.search-box{position:absolute;left:25px;top:383px;width:399px;height:62px;background:var(--white);border:3px solid #444;z-index:4;display:flex;align-items:center}
.search-box span{flex:1;padding-left:18px;font-size:16px;color:var(--text-dark)}
.search-box .search-btn{width:59px;height:100%;border-left:1px solid #ccc;display:flex;align-items:center;justify-content:center;color:#333}
.venue-card{position:absolute;left:25px;width:400px;height:99px;background:var(--white)}
.venue-card--first{box-shadow:0 1px 4px rgba(0,0,0,.15)}
.venue-name{position:absolute;left:16px;top:18px;font-size:21px;color:var(--brand-red)}
.venue-meta{position:absolute;left:14px;top:56px;display:flex;align-items:center;font-size:15px;color:var(--text-mid)}
.venue-meta .meta{display:flex;align-items:center;margin-right:22px}
.venue-meta .meta:last-child{margin-right:0}
.venue-meta svg{margin-right:9px;color:#777}
.section-title{position:absolute;left:24px;top:270px;font-size:25px;color:var(--text-dark);letter-spacing:.5px}
.list-card{position:absolute;left:25px;top:318px;width:400px;height:464px;background:var(--white)}
.list-head{height:57px;border-bottom:1px solid var(--border-light);display:flex;align-items:center;padding-left:14px;color:var(--accent-orange);font-size:20px}
.list-head svg{margin-right:10px}
.soup-row{position:relative;height:101px;border-bottom:1px solid var(--border-light)}
.soup-row:last-child{border-bottom:none}
.thumb{position:absolute;left:14px;top:17px;width:73px;height:65px;border:1px solid #ddd;background:var(--white)}
.thumb i{position:absolute;left:8px;top:14px;width:56px;height:32px;border-radius:0 0 28px 28px}
.thumb--tomato i{background:#d9442a}.thumb--lentil i{background:#dd7b2c}.thumb--veg i{background:#c79a54}.thumb--pea i{background:#b9cf7a}
.soup-name{position:absolute;left:104px;top:38px;font-size:18px;color:var(--text-dark);letter-spacing:.3px}
.fav{position:absolute;right:22px;top:38px}
.cafe-card{position:absolute;left:25px;top:318px;width:400px;height:464px;background:var(--white)}
.cafe-row{position:relative;height:102px;border-bottom:1px solid var(--border-light)}
.cafe-row:nth-child(4){height:106px}
.cafe-photo{position:absolute;left:14px;top:18px;width:72px;height:64px;background:linear-gradient(135deg,#6b5e52,#a89888 45%,#4c4a3c)}
.cafe-name{position:absolute;left:104px;top:27px;font-size:19px;color:var(--text-dark)}
.cafe-price{position:absolute;left:104px;top:54px;font-size:19px;color:var(--price-green)}
.cafe-dist{position:absolute;right:14px;top:30px;width:76px;text-align:center;font-size:15px;color:var(--text-mid)}
.cafe-dist svg{display:block;margin:0 auto 4px;color:#333}
.bottom-nav{position:absolute;left:0;top:815px;width:100%;height:85px;background:var(--nav-dark);box-shadow:0 -4px 8px rgba(0,0,0,.08)}
.nav-item{position:absolute;top:14px;transform:translateX(-50%);text-align:center;color:var(--white);font-weight:700;font-size:16px;white-space:nowrap}
.nav-item svg{display:block;margin:0 auto 7px;color:var(--accent-orange)}
.nav-center{position:absolute;left:225px;top:10px;width:52px;height:52px;transform:translateX(-50%);border-radius:50%;background:var(--brand-red)}
</style>
</head>
<body>
<svg width="0" height="0" style="position:absolute">
  <defs>
    <symbol id="i-pin" viewBox="0 0 24 24"><path fill="currentColor" d="M12 1.5C7.9 1.5 4.8 4.6 4.8 8.6c0 5.3 7.2 13.9 7.2 13.9s7.2-8.6 7.2-13.9c0-4-3.1-7.1-7.2-7.1zm0 10.2a3.1 3.1 0 110-6.2 3.1 3.1 0 010 6.2z"/></symbol>
    <symbol id="i-heart" viewBox="0 0 24 24"><path fill="currentColor" d="M12 21.3l-1.5-1.3C5 15.1 2 12.3 2 8.6 2 5.6 4.4 3.2 7.4 3.2c1.8 0 3.5.8 4.6 2.1 1.1-1.3 2.8-2.1 4.6-2.1 3 0 5.4 2.4 5.4 5.4 0 3.7-3 6.5-8.5 11.4z"/></symbol>
    <symbol id="i-heart-line" viewBox="0 0 24 24"><path fill="none" stroke="currentColor" stroke-width="1.5" d="M12 20.3l-1.2-1.1C5.6 14.6 2.8 12.1 2.8 8.8c0-2.6 2-4.8 4.6-4.8 1.8 0 3.4 1 4.6 2.6 1.2-1.6 2.8-2.6 4.6-2.6 2.6 0 4.6 2.2 4.6 4.8 0 3.3-2.8 5.8-8 10.4z"/></symbol>
    <symbol id="i-star" viewBox="0 0 24 24"><circle cx="12" cy="12" r="10" fill="none" stroke="currentColor" stroke-width="2"/><polygon fill="currentColor" points="12,5.8 13.9,9.7 18.1,10.2 15,13.1 15.8,17.3 12,15.2 8.2,17.3 9,13.1 5.9,10.2 10.1,9.7"/></symbol>
    <symbol id="i-person" viewBox="0 0 24 24"><circle cx="12" cy="7" r="5" fill="currentColor"/><path fill="currentColor" d="M3 23c0-5.5 4-9 9-9s9 3.5 9 9z"/></symbol>
    <symbol id="i-gear" viewBox="0 0 24 24"><circle cx="12" cy="12" r="8" fill="none" stroke="currentColor" stroke-width="5" stroke-dasharray="3.6 2.7"/><circle cx="12" cy="12" r="6.5" fill="currentColor"/><circle cx="12" cy="12" r="2.6" fill="#333"/></symbol>
    <symbol id="i-bowl" viewBox="0 0 36 32"><path fill="none" stroke="currentColor" stroke-width="1.8" d="M12 11c-2-2.5 2-4 0-7M18 11c-2-2.5 2-4 0-7M24 11c-2-2.5 2-4 0-7"/><rect x="2" y="14" width="32" height="3" fill="currentColor"/><rect x="3" y="19" width="30" height="3" fill="currentColor"/><rect x="6" y="24" width="24" height="3" fill="currentColor"/><rect x="11" y="29" width="14" height="2" fill="currentColor"/></symbol>
    <symbol id="i-home" viewBox="0 0 24 24"><path fill="currentColor" d="M12 2L1 12h3v10h6v-6h4v6h6V12h3z"/></symbol>
    <symbol id="i-search" viewBox="0 0 24 24"><circle cx="10" cy="10" r="7" fill="none" stroke="currentColor" stroke-width="3"/><path stroke="currentColor" stroke-width="3.4" stroke-linecap="round" d="M15.5 15.5L21.5 21.5"/></symbol>
  </defs>
</svg>

<div class="stage">

  <!-- Screen 1: nearby map -->
  <section class="phone phone--map">
    <header class="app-header"><h1 class="app-title">Ladles and Lanterns</h1></header>
    <div class="brand-dot"></div>
    <div class="map-area" role="img" aria-label="Street map of the surrounding city with a pin marking the user's location"></div>
    <div class="search-box"><span>Find Nearest Restaurant</span><div class="search-btn"><svg width="20" height="20"><use href="#i-search"/></svg></div></div>

    <article class="venue-card venue-card--first" style="top:469px">
      <h2 class="venue-name">Restaurant Name</h2>
      <div class="venue-meta">
        <span class="meta"><svg width="25" height="22"><use href="#i-bowl"/></svg>Soup Name</span>
        <span class="meta"><svg width="24" height="24"><use href="#i-star"/></svg>10% off</span>
        <span class="meta"><svg width="18" height="20"><use href="#i-pin"/></svg>5km away</span>
      </div>
    </article>
    <article class="venue-card" style="top:580px">
      <h2 class="venue-name">Restaurant Name</h2>
      <div class="venue-meta">
        <span class="meta"><svg width="25" height="22"><use href="#i-bowl"/></svg>Soup Name</span>
        <span class="meta"><svg width="24" height="24"><use href="#i-star"/></svg>10% off</span>
        <span class="meta"><svg width="18" height="20"><use href="#i-pin"/></svg>5km away</span>
      </div>
    </article>
    <article class="venue-card" style="top:692px">
      <h2 class="venue-name">Restaurant Name</h2>
      <div class="venue-meta">
        <span class="meta"><svg width="25" height="22"><use href="#i-bowl"/></svg>Soup Name</span>
        <span class="meta"><svg width="24" height="24"><use href="#i-star"/></svg>10% off</span>
        <span class="meta"><svg width="18" height="20"><use href="#i-pin"/></svg>5km away</span>
      </div>
    </article>

    <nav class="bottom-nav">
      <div class="nav-item" style="left:51px"><svg width="36" height="32"><use href="#i-bowl"/></svg>Soups</div>
      <div class="nav-item" style="left:159px"><svg width="32" height="32"><use href="#i-star"/></svg>Specials</div>
      <div class="nav-item" style="left:274px"><svg width="32" height="32" style="padding:4px"><use href="#i-person"/></svg>Account</div>
      <div class="nav-item" style="left:386px"><svg width="32" height="32" style="padding:4px"><use href="#i-gear"/></svg>Settings</div>
    </nav>
  </section>

  <!-- Screen 2: restaurant soup list -->
  <section class="phone phone--menu">
    <header class="app-header"><h1 class="app-title">Ladles and Lanterns</h1></header>
    <div class="brand-dot"></div>
    <div class="hero" role="img" aria-label="Photo of a bowl of vegetable soup with herbs on a wooden table"></div>
    <h2 class="section-title">Restaurant Name</h2>
    <div class="list-card">
      <div class="list-head"><svg width="26" height="24"><use href="#i-bowl"/></svg>Soup Name Type</div>
      <div class="soup-row"><div class="thumb thumb--tomato" role="img" aria-label="Tomato soup"><i></i></div><span class="soup-name">Carrot+ Corrainder</span><svg class="fav" width="26" height="26" style="color:var(--brand-red)"><use href="#i-heart"/></svg></div>
      <div class="soup-row"><div class="thumb thumb--lentil" role="img" aria-label="Lentil soup"><i></i></div><span class="soup-name">Carrot+ Corrainder</span><svg class="fav" width="26" height="26" style="color:#444"><use href="#i-heart-line"/></svg></div>
      <div class="soup-row"><div class="thumb thumb--veg" role="img" aria-label="Vegetable broth"><i></i></div><span class="soup-name">Carrot+ Corrainder</span><svg class="fav" width="26" height="26" style="color:#444"><use href="#i-heart-line"/></svg></div>
      <div class="soup-row"><div class="thumb thumb--pea" role="img" aria-label="Pea soup"><i></i></div><span class="soup-name">Carrot+ Corrainder</span><svg class="fav" width="26" height="26" style="color:#444"><use href="#i-heart-line"/></svg></div>
    </div>
    <nav class="bottom-nav">
      <div class="nav-item" style="left:51px"><svg width="36" height="32"><use href="#i-bowl"/></svg>Soups</div>
      <div class="nav-item" style="left:159px"><svg width="32" height="32"><use href="#i-star"/></svg>Specials</div>
      <div class="nav-item" style="left:274px"><svg width="32" height="32" style="padding:2px"><use href="#i-heart"/></svg>Favourite</div>
      <div class="nav-item" style="left:386px"><svg width="32" height="32" style="padding:4px"><use href="#i-gear"/></svg>Settings</div>
    </nav>
  </section>

  <!-- Screen 3: soup detail, cafés serving it -->
  <section class="phone phone--detail">
    <header class="app-header"><h1 class="app-title">Ladles and Lanterns</h1></header>
    <div class="brand-dot"></div>
    <div class="hero" role="img" aria-label="Photo of a bowl of vegetable soup with herbs on a wooden table"></div>
    <h2 class="section-title">Carrot+ Corainder</h2>
    <div class="cafe-card">
      <div class="cafe-row"><div class="cafe-photo" role="img" aria-label="Cafe kitchen"></div><span class="cafe-name">Cafe Name</span><span class="cafe-price">$5.00</span><span class="cafe-dist"><svg width="18" height="20"><use href="#i-pin"/></svg>5km away</span></div>
      <div class="cafe-row"><div class="cafe-photo" role="img" aria-label="Cafe kitchen"></div><span class="cafe-name">Cafe Name</span><span class="cafe-price">$5.00</span><span class="cafe-dist"><svg width="18" height="20"><use href="#i-pin"/></svg>5km away</span></div>
      <div class="cafe-row"><div class="cafe-photo" role="img" aria-label="Cafe kitchen"></div><span class="cafe-name">Cafe Name</span><span class="cafe-price">$5.00</span><span class="cafe-dist"><svg width="18" height="20"><use href="#i-pin"/></svg>5km away</span></div>
      <div class="cafe-row"><div class="cafe-photo" role="img" aria-label="Cafe kitchen"></div><span class="cafe-name">Cafe Name</span><span class="cafe-price">$5.00</span><span class="cafe-dist"><svg width="18" height="20"><use href="#i-pin"/></svg>5km away</span></div>
    </div>
    <nav class="bottom-nav">
      <div class="nav-item" style="left:46px"><svg width="32" height="32" style="padding:2px"><use href="#i-home"/></svg>Home</div>
      <div class="nav-item" style="left:134px"><svg width="32" height="32" style="padding:3px"><use href="#i-search"/></svg>Search</div>
      <div class="nav-center"></div>
      <div class="nav-item" style="left:304px"><svg width="32" height="32" style="padding:2px"><use href="#i-heart"/></svg>Favourite</div>
      <div class="nav-item" style="left:401px"><svg width="32" height="32" style="padding:4px"><use href="#i-gear"/></svg>Settings</div>
    </nav>
  </section>

</div>
</body>
</html>
```